Design Business Card & PPT & DOC

Using the attached logo, I want a complete design package: Business cards, a power point template (home page and an inside page) and a Word document template for the customer relationship. (proposals, offers, etc.)
Address: Vantor Learning
Street Dr. Mircea Tolanu no. 42, 3rd floor, Sector 2, Bucharest, postal code, 072318;
E-mail: info@[login to view URL]; Tel: 0317 869 120; Fax: 0375 413 986
[login to view URL]
--------

About Company
Vantor Learning delivers authorized professional training courses in
open or in-house regime in the fields of: sales, negotiation, management, marketing,
persuasion, human resources, trainer, project management, communication, oratory,
access to European funds, taxation as well as a full range of resource services
human: teambuilding, consulting, executive coaching, etc.

```html
<!DOCTYPE html>
<html lang="en">
<head>
<meta charset="utf-8">
<title>Vantor Learning – Business Card &amp; Envelope</title>
<link rel="stylesheet" href="https://fonts.googleapis.com/css2?family=Open+Sans:wght@400;700&display=swap">
<style>
  :root {
    --red: #e53333;
    --red-deep: #d62828;
    --black: #1f1f1f;
    --charcoal: #3a3a3c;
    --white: #ffffff;
    --ink: #2b2b2b;
    --backdrop: #eeeeef;
  }
  * { margin: 0; padding: 0; box-sizing: border-box; }
  html, body {
    width: 1200px; height: 848px; overflow: hidden;
    background: var(--backdrop);
    font-family: "Open Sans", sans-serif;
  }
  .stage { position: relative; width: 1200px; height: 848px; }

  /* Business card */
  .business-card {
    position: absolute; left: 285px; top: 109px;
    width: 627px; height: 316px;
    background: var(--white);
    box-shadow: 0 2px 6px rgba(0,0,0,0.12);
    overflow: hidden;
  }
  .brand { position: absolute; display: flex; align-items: center; gap: 14px; }
  .business-card .brand { left: 29px; top: 31px; }
  .brand-dot {
    width: 86px; height: 86px; border-radius: 50%;
    background: var(--red); flex: none;
  }
  .brand-name {
    color: var(--red); font-weight: 700; font-size: 18px; line-height: 1;
  }
  .contact-list { position: absolute; left: 40px; top: 169px; list-style: none; }
  .contact-item {
    display: flex; align-items: center; gap: 2px;
    height: 23px; font-size: 13px; color: var(--ink);
  }
  .icon { width: 15px; height: 15px; flex: none; }
  .address {
    position: absolute; left: 318px; top: 222px;
    display: flex; gap: 6px; align-items: flex-start;
    font-size: 12px; line-height: 15px; color: var(--ink);
  }
  .address .icon { margin-top: 1px; width: 16px; height: 18px; }
  .card-bands { position: absolute; left: 0; bottom: 0; width: 627px; height: 30px; }

  /* Envelope */
  .envelope {
    position: absolute; left: 285px; top: 456px;
    width: 627px; height: 317px;
    box-shadow: 0 2px 6px rgba(0,0,0,0.12);
  }
  .envelope-art { position: absolute; inset: 0; width: 627px; height: 317px; }
  .envelope .brand { left: 110px; top: 133px; }
</style>
</head>
<body>
<main class="stage">

  <section class="business-card" aria-label="Business card front">
    <div class="brand">
      <span class="brand-dot"></span>
      <span class="brand-name">Vantor Learning</span>
    </div>

    <ul class="contact-list">
      <li class="contact-item">
        <svg class="icon" viewBox="0 0 16 16"><rect width="16" height="16" rx="3" fill="var(--red)"/><path d="M4 6c0-1.2 1.8-2 4-2s4 .8 4 2l-1.5 .6L9.5 5.8H6.5L5.5 6.6z M5 8h6l1 4H4z" fill="#fff"/></svg>
        <span>0317 869 120</span>
      </li>
      <li class="contact-item">
        <svg class="icon" viewBox="0 0 16 16"><rect width="16" height="16" rx="3" fill="var(--red)"/><rect x="5" y="3" width="6" height="3" fill="#fff"/><rect x="3" y="6.5" width="10" height="5" rx="1" fill="#fff"/><rect x="5" y="10" width="6" height="3" fill="#fff" stroke="var(--red)" stroke-width=".8"/></svg>
        <span>0375 413 986</span>
      </li>
      <li class="contact-item">
        <svg class="icon" viewBox="0 0 16 16"><rect width="16" height="16" rx="3" fill="var(--red)"/><rect x="3" y="4.5" width="10" height="7" fill="#fff"/><path d="M3 4.5l5 4 5-4" fill="none" stroke="var(--red)" stroke-width="1"/></svg>
        <span>info@vantorlearning.ro</span>
      </li>
      <li class="contact-item">
        <svg class="icon" viewBox="0 0 16 16"><rect width="16" height="16" rx="3" fill="var(--red)"/><g fill="none" stroke="#fff" stroke-width="1"><circle cx="8" cy="8" r="5"/><ellipse cx="8" cy="8" rx="2.2" ry="5"/><path d="M3 8h10M4 5.5h8M4 10.5h8"/></g></svg>
        <span>www.vantorlearning.ro</span>
      </li>
    </ul>

    <div class="address">
      <svg class="icon" viewBox="0 0 16 18"><rect width="16" height="18" rx="3" fill="var(--red)"/><path d="M8 3a3.5 3.5 0 0 0-3.5 3.5C4.5 9.5 8 14 8 14s3.5-4.5 3.5-7.5A3.5 3.5 0 0 0 8 3z" fill="#fff"/><circle cx="8" cy="6.5" r="1.3" fill="var(--red)"/></svg>
      <p>Street Dr. Mircea Tolanu no. 42, 3rd floor,<br>Sector 2, Bucharest, postal code, 072318</p>
    </div>

    <svg class="card-bands" viewBox="0 0 627 30" aria-hidden="true">
      <polygon class="band-black" points="0,0 340,0 320,30 0,30" fill="var(--black)"/>
      <polygon class="band-red" points="353,0 627,0 627,30 333,30" fill="var(--red)"/>
    </svg>
  </section>

  <section class="envelope" aria-label="Envelope back">
    <svg class="envelope-art" viewBox="0 0 627 317" aria-hidden="true">
      <rect class="envelope-body" width="627" height="317" fill="var(--red)"/>
      <polygon class="envelope-panel" points="14,44 26,96 600,96 612,44 612,317 14,317" fill="var(--white)"/>
      <rect class="envelope-flap" x="0" y="0" width="627" height="96" fill="var(--red)"/>
      <rect class="envelope-edge" x="612" y="0" width="15" height="317" fill="var(--red-deep)"/>
      <polygon class="fold-left-red" points="0,170 320,300 320,317 0,317" fill="var(--red)"/>
      <polygon class="fold-left-black" points="0,230 250,317 0,317" fill="var(--black)"/>
      <polygon class="fold-left-charcoal" points="0,262 160,317 0,317" fill="var(--charcoal)"/>
      <polygon class="fold-right-black" points="627,170 627,215 250,317 180,317" fill="var(--black)"/>
      <polygon class="fold-right-red" points="627,215 627,317 250,317" fill="var(--red)"/>
      <polygon class="fold-right-shade" points="627,260 627,317 420,317" fill="var(--red-deep)"/>
    </svg>
    <div class="brand">
      <span class="brand-dot"></span>
      <span class="brand-name">Vantor Learning</span>
    </div>
  </section>

</main>
</body>
</html>
```